Scrum Master & Agile IT Coach Needing Business Website

Hello, my name is Brent Holloway
I am a project manger, scrum master, & agile coach. I work with IT development teams on major projects for Fortune 500 companies . My project management business has a website and can be found here: www.tq-keystride.example

I have launched a new company, ALL focused on IT Agile Coaching, I am looking to have a website created for my new company - the name of the new company is: Pins and Dials - Agile IT Coaching and Training.
I have a logo and it is provided in the materials. I like to logo; I am open to different color pallets.

The website will have a total of 7 pages; I have content for 5 of the 7 pages prepared; the other 2 pages will say under construction.

Page 1 Who am I, What I do, My Experience
Demonstrated experience and progression from Scrum Master to
Program Manager to Coach

Page 2 Pins & Dials - Agile Team Coaching
teams working major IT projects, multiple months/years

Page 3 Coaching @ the Team Level

Page 4 Coaching @ the Program Level ; LYNQ BQR level

Pages 5 -6 Under Construction

Page 7 Presentations, Slide Decks, Reference Materials

Mentor Nook need to have this highlighted somewhere Monthly Blog
Updates

Industry/Entity Type

IT development

Coding

Coded - Design and coding required

Number of Pages Required

5+ page

Requirements
Must have
• the website must be bold - I want those who visit to remember coming to my coaching site
Nice to have
• nice to have will be a modern / futuristic website; I work with IT developers, I want a website they will like
Should not have
• should not be stiff - it should be professional but fun

```html
<!DOCTYPE html>
<html lang="en">
<head>
<meta charset="utf-8">
<title>Pins &amp; Dials – Agile IT Coaching &amp; Training</title>
<link href="https://fonts.googleapis.com/css2?family=Montserrat:wght@300;400;500;600;700;800;900&display=swap" rel="stylesheet">
<style>
:root{
  --navy:#1b4a96;
  --navy-deep:#153d80;
  --ink:#111111;
  --text:#7a7a7a;
  --mist:#eef1f6;
  --white:#ffffff;
  --badge-1:#2a4474;
  --badge-2:#f0a24e;
  --badge-3:#3aa8e0;
  --badge-4:#25385f;
  --badge-5:#f4b43a;
}
*{box-sizing:border-box;margin:0;padding:0}
html,body{width:1200px;height:3845px;overflow:hidden}
body{font-family:'Montserrat',sans-serif;background:var(--white);position:relative;color:var(--ink)}
.abs{position:absolute}
.brand{display:flex;align-items:center;gap:12px;color:var(--white);font-weight:800;font-size:30px;letter-spacing:.5px}
.brand .mark{width:26px;height:26px;background:currentColor}
.brand small{display:block;font-size:9px;font-weight:700;letter-spacing:1.5px;margin-top:2px}

/* header */
.site-header{left:0;top:0;width:1200px;height:80px;background:var(--navy)}
.site-header .brand{position:absolute;left:143px;top:14px}
.burger{position:absolute;left:1028px;top:28px;width:28px}
.burger span{display:block;height:4px;background:var(--white);margin-bottom:6px;border-radius:1px}

/* hero */
.hero{left:0;top:80px;width:1200px;height:502px;background:linear-gradient(110deg,#1d3e6e 0%,#3d6aa6 35%,#6d7d96 60%,#2e2a2a 100%)}
.hero-card{position:absolute;left:675px;top:75px;width:437px;height:320px;border:6px solid var(--white);background:rgba(40,30,28,.55);padding:55px 34px}
.hero-card h1{color:var(--white);font-size:31px;font-weight:800;line-height:34px;text-transform:uppercase}
.dots{position:absolute;left:996px;top:463px;display:flex;gap:7px;align-items:center}
.dots i{width:7px;height:7px;border-radius:50%;background:var(--white)}
.dots i.on{width:11px;height:11px;border:2px solid var(--white);background:var(--navy)}

/* about */
.about-photo{left:143px;top:690px;width:375px;height:458px;background:linear-gradient(160deg,#3c6a99,#a9b9c8 45%,#263b56)}
.about-photo .gap-v{position:absolute;left:156px;top:0;width:10px;height:200px;background:var(--white)}
.about-photo .gap-h{position:absolute;left:0;top:188px;width:166px;height:10px;background:var(--white)}
.portrait{left:393px;top:990px;width:125px;height:158px;background:var(--white);padding:10px}
.portrait div{width:100%;height:100%;background:linear-gradient(180deg,#8a9aa6,#5a3d2c)}
.about-text{left:567px;top:678px;width:488px}
.about-text h2{color:var(--navy);font-size:48px;font-weight:800;line-height:58px;white-space:nowrap}
.about-text h3{font-size:21px;font-weight:700;margin-top:4px}
.rule{width:30px;height:4px;background:var(--navy)}
.about-text .rule{margin-top:13px}
.about-text p{margin-top:38px;font-size:13.5px;font-weight:300;line-height:26.4px;color:var(--text);text-align:justify}
.btn{display:inline-block;background:var(--ink);color:var(--white);font-weight:700;font-size:14px;text-transform:uppercase}
.about-text .btn{margin-top:32px;padding:14px 20px}

.section-title{position:absolute;left:0;width:1200px;text-align:center;font-size:50px;font-weight:800;text-transform:uppercase}
.section-title .blue{color:var(--navy)}

/* badges */
.badges{left:0;top:1398px;width:1200px;height:150px}
.badge{position:absolute;top:10px;width:130px;height:130px;border-radius:50%}

/* profiles */
.profile{top:1624px;height:82px;color:var(--white);text-align:center;padding-top:20px}
.profile b{display:block;font-size:15px;font-weight:700}
.profile span{display:block;font-size:9.5px;margin-top:8px}
.profile.blue{background:var(--navy)}
.profile.dark{background:var(--ink)}

/* roles */
.roles{left:0;top:1706px;width:1200px;height:543px;background:linear-gradient(180deg,#ffffff,var(--mist))}
.role-card{position:absolute;width:211px;height:202px;border:3px solid #c9ccd2;border-radius:8px;background:var(--white);text-align:center;padding-top:28px}
.role-card strong{display:block;color:var(--navy);font-size:52px;font-weight:800;line-height:60px}
.role-card p{margin:12px auto 0;width:180px;font-size:17px;font-weight:600;line-height:23px}

/* experience */
.experience{left:0;top:2249px;width:1200px;height:557px;background:linear-gradient(120deg,#234f98,#1b4a96 50%,#2a5aa8)}
.exp-buttons{left:143px;top:2493px;width:439px}
.exp-buttons div{height:45px;border:1.5px solid rgba(255,255,255,.85);color:var(--white);font-weight:700;font-size:15px;text-align:center;line-height:42px;margin-bottom:15px}
.checklist{left:645px;top:2486px;width:430px;list-style:none;color:var(--white);font-size:12.5px;line-height:25px}
.checklist li{position:relative;padding-left:31px}
.checklist svg{position:absolute;left:0;top:7px}
.frame-tr{left:1055px;top:2119px;width:160px;height:254px;border:6px solid var(--white);border-right:none}
.frame-bl{left:-10px;top:2709px;width:168px;height:110px;border:6px solid var(--white);border-left:none;border-bottom:none}

/* play */
.play{left:0;top:2806px;width:1200px;height:502px;background:linear-gradient(90deg,#f3f5f9 0%,#e3e9f2 40%,#8fa5c2 65%,#3b4f6e 100%)}
.play-title{left:143px;top:2924px;font-size:49px;font-weight:800;line-height:60px;text-transform:uppercase}
.play-title .blue{color:var(--navy)}
.play .btn{position:absolute}

/* footer */
.site-footer{left:0;top:3308px;width:1200px;height:537px;background:linear-gradient(180deg,#f5f7fa,#ffffff)}
.site-footer .brand{position:absolute;left:0;width:1200px;justify-content:center;top:82px;color:var(--navy)}
.newsletter-title{left:143px;top:3523px;color:var(--navy);font-size:30px;font-weight:800;text-transform:uppercase}
.email{left:540px;top:3519px;width:373px;height:45px;border:1px solid #c7ccd4;background:var(--white);font-size:12px;padding:15px 22px;color:#333}
.subscribe{left:922px;top:3519px;width:133px;height:45px;background:var(--ink);color:var(--white);font-size:14px;font-weight:700;text-align:center;line-height:45px}
.footer-nav{left:0;top:3622px;width:1200px;text-align:center;font-size:14.5px;font-weight:600;line-height:28px}
.footer-nav i{font-style:normal;margin:0 10px}
.copyright{left:0;top:3702px;width:1200px;text-align:center;font-size:12px;color:#666}
.social{left:538px;top:3760px;display:flex;gap:16px}
.social span{width:30px;height:30px;border-radius:50%;background:var(--ink)}
</style>
</head>
<body>

<header class="site-header abs">
  <div class="brand"><span class="mark"></span><div>PINS &amp; DIALS<small>AGILE IT COACHING &amp; TRAINING L.L.C</small></div></div>
  <div class="burger"><span></span><span></span><span></span></div>
</header>

<section class="hero abs" role="img" aria-label="Hands on a laptop in front of a projected project management timeline">
  <div class="hero-card"><h1>Demonstrate experience and progression from scrum master to program manager to coach</h1></div>
  <div class="dots"><i></i><i class="on"></i><i></i></div>
</section>

<div class="about-photo abs" role="img" aria-label="Team reviewing charts and reports at a desk">
  <div class="gap-v"></div><div class="gap-h"></div>
</div>
<div class="portrait abs"><div role="img" aria-label="Portrait of Brent Holloway"></div></div>
<div class="about-text abs">
  <h2>BRENT HOLLOWAY</h2>
  <h3>Senior Scrum Master &amp; Team Agile Coach</h3>
  <div class="rule"></div>
  <p>Lorem ipsum dolor sit amet, consectetur adipiscing elit, sed do eiusmod tempor incididunt ut labore et dolore magna aliqua. Quis ipsum suspendisse ultrices gravida. Risus commodo viverra maecenas accumsan lacus vel facilisis. Lorem ipsum dolor sit amet, consectetur adipiscing elit, sed do eiusmod tempor incididunt ut labore et dolore magna aliqua. Quis ipsum suspendisse ultrices gravida. Risus commodo viverra maecenas accumsan lacus vel facilisis. Lorem ipsum dolor sit amet, consectetur adipiscing elit, sed do eiusmod tempor incididunt ut labore et dolore magna aliqua.</p>
  <span class="btn">Read More</span>
</div>

<h2 class="section-title" style="top:1266px"><span class="blue">Coaching</span> Designations</h2>
<div class="rule" style="position:absolute;left:585px;top:1341px"></div>

<div class="badges abs" role="img" aria-label="Certification badges">
  <div class="badge" style="left:145px;background:var(--badge-1)"></div>
  <div class="badge" style="left:330px;background:var(--badge-2)"></div>
  <div class="badge" style="left:517px;background:var(--badge-3)"></div>
  <div class="badge" style="left:705px;background:var(--badge-4)"></div>
  <div class="badge" style="left:898px;background:var(--badge-5)"></div>
</div>

<div class="profile blue abs" style="left:0;width:397px"><b>SPRINT GUILD PROFILE</b><span>https://www.sprintguild.example/profile/bholloway10</span></div>
<div class="profile dark abs" style="left:401px;width:397px"><b>CRESTMARK PROFILE</b><span>https://www.crestmark.example/users/brent-holloway</span></div>
<div class="profile blue abs" style="left:803px;width:397px"><b>LYNQ TIERED AGILE ALLIANCE PROFILE</b><span>https://tieredagile.example/profile/bholloway-0082</span></div>

<section class="roles abs">
  <h2 class="section-title" style="top:94px"><span class="blue">Roles I have</span> held</h2>
  <div class="rule" style="position:absolute;left:585px;top:167px"></div>
  <div class="role-card" style="left:143px;top:261px"><strong>01</strong><p>Sr. Scrum Master</p></div>
  <div class="role-card" style="left:378px;top:230px"><strong>02</strong><p>Advanced LYNQ Scrum Master</p></div>
  <div class="role-card" style="left:610px;top:261px"><strong>03</strong><p>Hybrid Scrum Master/ Project Manager</p></div>
  <div class="role-card" style="left:845px;top:230px"><strong>04</strong><p>Business (Finance Transformation Program Manager</p></div>
</section>

<section class="experience abs" role="img" aria-label="Blue-toned photo of a developer at work">
  <h2 class="section-title" style="top:90px;color:#fff">What is my experience</h2>
  <div class="rule" style="position:absolute;left:585px;top:161px;background:#fff"></div>
</section>
<div class="exp-buttons abs">
  <div>As a LYNQ Adv Scrum Master, I</div>
  <div>As a Hybrid Scrum Master / Project Manager, I</div>
  <div>Business Transformation Program Manager</div>
</div>
<ul class="checklist abs">
  <li><svg width="13" height="11" viewBox="0 0 13 11"><path d="M1 6l4 4 7-9" fill="none" stroke="#fff" stroke-width="2.4"/></svg>Stand up teams</li>
  <li><svg width="13" height="11" viewBox="0 0 13 11"><path d="M1 6l4 4 7-9" fill="none" stroke="#fff" stroke-width="2.4"/></svg>Run development efforts concurrently leading<br>multiple teams</li>
  <li><svg width="13" height="11" viewBox="0 0 13 11"><path d="M1 6l4 4 7-9" fill="none" stroke="#fff" stroke-width="2.4"/></svg>Run LYNQ ceremonies</li>
  <li><svg width="13" height="11" viewBox="0 0 13 11"><path d="M1 6l4 4 7-9" fill="none" stroke="#fff" stroke-width="2.4"/></svg>Scrum of Scrums facilitator</li>
  <li><svg width="13" height="11" viewBox="0 0 13 11"><path d="M1 6l4 4 7-9" fill="none" stroke="#fff" stroke-width="2.4"/></svg>PI Planning team facilitator (multiple teams on BQR)</li>
  <li><svg width="13" height="11" viewBox="0 0 13 11"><path d="M1 6l4 4 7-9" fill="none" stroke="#fff" stroke-width="2.4"/></svg>Teach and coach to advanced development team strategies</li>
  <li><svg width="13" height="11" viewBox="0 0 13 11"><path d="M1 6l4 4 7-9" fill="none" stroke="#fff" stroke-width="2.4"/></svg>Lead program level communications and business status<br>updates on behalf of the team</li>
</ul>
<div class="frame-tr abs"></div>
<div class="frame-bl abs"></div>

<section class="play abs" role="img" aria-label="Two colleagues reviewing code on a monitor">
  <span class="btn" style="left:143px;top:328px;padding:13px 21px">Click Here</span>
</section>
<h2 class="play-title abs"><span class="blue">Where does</span><br>coaching come<br><span class="blue">in to play</span></h2>

<footer class="site-footer abs">
  <div class="brand"><span class="mark"></span><div>PINS &amp; DIALS<small>AGILE IT COACHING &amp; TRAINING L.L.C</small></div></div>
</footer>
<h3 class="newsletter-title abs">Sign up newsletter</h3>
<div class="email abs">Enter Email</div>
<div class="subscribe abs">SUBSCRIBE</div>
<nav class="footer-nav abs">
  WHO AM I<i>/</i>AGILE TEAM COACHING<i>/</i>COACHING @ THE TEAM LEVEL<i>/</i>COACHING @ THE PROGRAM LEVEL;<br>
  LYNQ BQR LEVEL<i>/</i>PRESENTATIONS<i>/</i>MONTHLY BLOG
</nav>
<p class="copyright abs">© 2022 Brent Holloway. All rights reserved.Privacy &nbsp;|&nbsp; Terms of Use</p>
<div class="social abs"><span></span><span></span><span></span></div>

</body>
</html>
```